Plakat-Design für Blasmusik Konzert
Zielgruppe
Wir - die Tordinger Blasmusik e.V. - sind auf der Suche nach:
einem Plakatdesign in A1 & A2 und passendem
Ticket-Design DIN lang quer inkl. Perforierung und 2x Nummerierung
für unser Konzert 2019 mit dem Motto:
'NIGHTS OF WONDER'.
Das Konzert wird einen weiten Rahmen von Henrik Dallmann und Brisko hin zu Bernd Falkenrath und Tom Kellin. Auch Titel aus dem Bereich Filmmusik wird es geben. Also ein bunter Abend mit Gesang und Showlicht.
Wir freuen uns auf eure Ideen!!!
Impressionen: www.tordinger-blasmusik.de
Aufgabenstellung
Stichworte: Bunt, Modern, Edel
Facts:
Samstag 05.10.2019 Beginn 19:00
Aula im Schulzentrum, Weidenbrück am See
Eintritt 15€, Kinder bis einschließlich 8 Jahre Eintritt frei.
'Mehr Informationen unter www.tordinger-blasmusik.de und auf Plaudernet'
Für Ticket: Einlass ab 18:30 Uhr. Freie Platzwahl.
Irgendwo auf dem Plakat muss Platz für die dezente Nennung von 2-3 Sponsoren vorgesehen werden. Diese würden wir nachträglich einfügen. Auch ein 'Find us on Plaudernet'-Icon wäre cool.
Die Druckdateien (CMYK) sind mit entsprechendem Beschnitt gemäß Vorgabe von 'flott-gedruckt-jetzt' anzulegen und als Vector-Datei sowie PDF zu übergeben.

```html
<!DOCTYPE html>
<html lang="de">
<head>
<meta charset="utf-8">
<title>Nights of Wonder – Tordinger Blasmusik e.V.</title>
<link rel="stylesheet" href="https://fonts.googleapis.com/css2?family=Fira+Sans:ital,wght@0,500;0,700;1,500;1,600;1,700&family=Great+Vibes&display=swap">
<style>
  :root {
    --stage: #d9d9d9;
    --poster-bg: #4b4b4d;
    --gold: #e6bb55;
    --white: #ffffff;
    --ink-dark: #3f3f41;
  }
  html, body {
    margin: 0;
    padding: 0;
    width: 1200px;
    height: 1200px;
    overflow: hidden;
    background: var(--stage);
  }
  .poster {
    position: absolute;
    left: 193px;
    top: 20px;
    width: 814px;
    height: 1160px;
    overflow: hidden;
    background: var(--poster-bg);
    font-family: "Fira Sans", Arial, sans-serif;
    color: var(--white);
  }
  .color-haze {
    position: absolute;
    left: 0; top: 280px;
    width: 814px; height: 790px;
    background:
      radial-gradient(ellipse 200px 190px at 80px 540px, rgba(240,30,90,1), transparent 72%),
      radial-gradient(ellipse 200px 200px at 250px 660px, rgba(230,40,170,1), transparent 72%),
      radial-gradient(ellipse 190px 220px at 420px 640px, rgba(110,50,210,1), transparent 72%),
      radial-gradient(ellipse 190px 230px at 560px 500px, rgba(20,110,220,1), transparent 72%),
      radial-gradient(ellipse 170px 230px at 700px 580px, rgba(30,200,170,1), transparent 72%),
      radial-gradient(ellipse 190px 260px at 770px 320px, rgba(110,210,50,1), transparent 72%),
      radial-gradient(ellipse 150px 200px at 790px 150px, rgba(235,205,40,.9), transparent 72%),
      radial-gradient(ellipse 190px 180px at 790px 700px, rgba(250,190,20,1), transparent 72%),
      radial-gradient(ellipse 190px 220px at 90px 330px, rgba(250,110,30,.9), transparent 72%),
      radial-gradient(ellipse 210px 190px at 60px 140px, rgba(250,210,60,.6), transparent 72%);
    filter: blur(8px);
  }
  .band-illustration {
    position: absolute;
    left: 61px; top: 172px;
    width: 744px; height: 752px;
    background: linear-gradient(180deg, rgba(90,90,92,.12), rgba(140,140,142,.18) 50%, rgba(90,90,92,.08));
  }
  .club-name {
    position: absolute;
    left: 20px; top: 58px;
    font-weight: 700;
    font-size: 42px;
    line-height: 1.05;
    margin: 0;
  }
  .club-name span { display: block; font-size: 33px; }
  .event-facts {
    position: absolute;
    right: 22px; top: 30px;
    text-align: right;
  }
  .event-date {
    margin: 0;
    font-weight: 500;
    font-size: 44px;
    color: var(--gold);
    line-height: 1.1;
  }
  .event-start {
    margin: 0;
    font-weight: 500;
    font-size: 42px;
    line-height: 1.15;
  }
  .facts-rule {
    width: 285px;
    height: 2px;
    background: var(--gold);
    margin: 12px 0 12px auto;
  }
  .event-venue {
    margin: 0;
    font-style: italic;
    font-weight: 500;
    font-size: 24px;
    line-height: 1.25;
  }
  .event-title {
    position: absolute;
    left: 80px; top: 285px;
    width: 660px;
    margin: 0;
    font-family: "Great Vibes", cursive;
    font-weight: 400;
    text-align: center;
    line-height: .95;
    text-shadow: 0 3px 8px rgba(0,0,0,.35);
  }
  .event-title .line-1 { display: block; font-size: 190px; padding-left: 110px; }
  .event-title .line-2 { display: block; font-size: 160px; margin-top: -10px; }
  .concert-year {
    position: absolute;
    left: 52px; top: 693px;
    margin: 0;
    font-style: italic;
    font-weight: 600;
    font-size: 34px;
  }
  .ticket-price {
    position: absolute;
    left: 278px; top: 680px;
    width: 232px; height: 232px;
    border-radius: 50%;
    background: var(--ink-dark);
    border: 6px solid var(--gold);
    box-sizing: border-box;
    display: flex;
    flex-direction: column;
    align-items: center;
    justify-content: center;
    font-weight: 500;
    font-size: 46px;
    line-height: 1.15;
    box-shadow: 0 4px 10px rgba(0,0,0,.4);
  }
  .ticket-price em { font-style: italic; }
  .lineup {
    position: absolute;
    left: 0; top: 948px;
    width: 814px;
    text-align: center;
    margin: 0;
    font-style: italic;
    font-weight: 600;
    font-size: 27px;
    line-height: 1.2;
  }
  .fine-print {
    position: absolute;
    left: 0; top: 1030px;
    width: 814px;
    text-align: center;
    margin: 0;
    font-style: italic;
    font-size: 15px;
  }
  .info-band {
    position: absolute;
    left: 0; top: 1060px;
    width: 814px; height: 100px;
    background: var(--gold);
  }
  .info-label {
    position: absolute;
    left: 12px; top: 8px;
    margin: 0;
    font-size: 14px;
    font-weight: 500;
  }
  .info-social, .info-web {
    position: absolute;
    left: 12px;
    margin: 0;
    font-weight: 500;
    font-size: 23px;
  }
  .info-social { top: 30px; display: flex; align-items: center; gap: 6px; }
  .info-social .mark {
    width: 14px; height: 14px;
    background: var(--white);
  }
  .info-web { top: 60px; }
  .sponsor-badge {
    position: absolute;
    top: 24px;
    width: 96px; height: 56px;
    background: var(--white);
  }
  .sponsor-1 { left: 500px; }
  .sponsor-2 { left: 606px; }
  .sponsor-3 { left: 706px; }
</style>
</head>
<body>
  <main class="poster">
    <div class="color-haze"></div>
    <div class="band-illustration" role="img" aria-label="Illustration einer Band: Saxofonist, Trompeter, Schlagzeuger und Notenständer in Grau- und Goldtönen"></div>

    <h2 class="club-name">Tordinger<span>Blasmusik e.V.</span></h2>

    <section class="event-facts">
      <p class="event-date">Sa. 05.10.2019</p>
      <p class="event-start">Beginn: 19.00</p>
      <div class="facts-rule"></div>
      <p class="event-venue">Aula im Schulzentrum,<br>Weidenbrück am See</p>
    </section>

    <h1 class="event-title"><span class="line-1">Nights</span><span class="line-2">of Wonder</span></h1>

    <p class="concert-year">Konzert 2019</p>

    <div class="ticket-price"><span>Eintritt</span><em>15€*</em></div>

    <p class="lineup">Henrik Dallmann…Brisko…Bernd Falkenrath…Tom Kellin<br>Bunter Abend mit Gesang und Showlicht</p>

    <p class="fine-print">*Kinder bis einschließlich 8 Jahre Eintritt frei. Für Ticket: Einlass ab 18:30 Uhr. Freie Platzwahl.</p>

    <footer class="info-band">
      <p class="info-label">Mehr Informationen :</p>
      <p class="info-social"><span class="mark"></span>plaudernet.de/Tordinger-Blasmusik-eV</p>
      <p class="info-web">www.tordinger-blasmusik.de</p>
      <div class="sponsor-badge sponsor-1"></div>
      <div class="sponsor-badge sponsor-2"></div>
      <div class="sponsor-badge sponsor-3"></div>
    </footer>
  </main>
</body>
</html>
```